Author needs a new book, Kindle and Audiobook cover design

I updated and re-edited a book I wrote 25 years ago but now realize the title and design did not get the job done. I am seeking a book, Kindle and audiobook design that will make me stand out. The final design will pop while being sensitive to the nature of the subject. The title of the book is Quiet Lanterns. Subtitle: Ways to Notice and Step Away From Harmful Circles While Keeping Steady Belief by Dorian T. Wexcombe. I am wanting to get the attention of people who have been damaged by a church relationship that started well but ended badly.
Updates

The book title is: Quiet Lanterns. The Subtitle is: Ways To Notice and Step Away From Harmful Circles While Keeping Steady Belief. The dimension is 6x9 (150 pages) and I am the author: Dorian T. Wexcombe

Target Market(s)

People with a church experience; church leadership. Religious abuse victims.

Industry/Entity Type

Christian

Font styles to use
Serif

Colors

Designer to choose colors to be used in the design.

Requirements
Nice to have
• I am not married to the Serif font if another design works better.

```html
<!DOCTYPE html>
<html lang="en">
<head>
<meta charset="utf-8">
<title>Quiet Lanterns – Cover Wrap</title>
<link href="https://fonts.googleapis.com/css2?family=Open+Sans:ital,wght@0,400;1,400;1,700&family=Roboto:wght@400;700;900&display=swap" rel="stylesheet">
<style>
:root{
  --page:#ffffff;
  --ink:#141414;
  --cover-dark:#16171a;
  --white:#ffffff;
  --title-red:#ee1c1c;
  --band-blue:#2a5fa8;
  --band-blue-dark:#1d3f78;
  --band-blue-light:#4f86cc;
  --photo-light:#b9b9b9;
  --photo-mid:#6d6d6d;
  --photo-dark:#2a2a2a;
}
*{margin:0;padding:0;box-sizing:border-box}
html,body{width:1200px;height:874px;overflow:hidden;background:var(--page)}
.wrap{position:relative;width:1200px;height:874px}
.cover{position:absolute;left:35px;top:24px;width:1130px;height:825px;background:var(--cover-dark);box-shadow:0 2px 8px rgba(0,0,0,.35)}

/* back cover */
.back{position:absolute;left:0;top:0;width:549px;height:825px;overflow:hidden}
.back-photo{position:absolute;inset:0;background:radial-gradient(ellipse 45% 55% at 48% 42%,rgba(150,150,150,.28),rgba(40,40,40,.12) 60%,transparent 80%)}
.praise{position:absolute;left:40px;width:470px;text-align:center;color:var(--white);font-family:"Open Sans",sans-serif}
.praise blockquote{font-style:italic;font-size:12.4px;line-height:17px}
.praise cite{display:block;font-style:normal;font-size:12.6px;line-height:17px;margin-top:6px}
.praise-1{top:30px}
.praise-2{top:200px}
.praise-3{top:325px}
.praise-4{top:450px}
.author-photo{position:absolute;left:36px;top:660px;width:131px;height:131px;border-radius:50%;border:4px solid #8a8a8a;background:radial-gradient(circle at 50% 45%,#c89a84,#8a6352 70%,#5a4a44)}
.bio{position:absolute;left:180px;top:657px;width:336px;height:137px;background:var(--white);color:var(--ink);font-family:"Open Sans",sans-serif;font-style:italic;font-size:12.2px;line-height:16.5px;text-align:center;padding:16px 18px}

/* spine */
.spine{position:absolute;left:549px;top:0;width:33px;height:825px;background:linear-gradient(90deg,var(--band-blue-dark),var(--band-blue-light) 50%,var(--band-blue-dark));border-right:1px solid #d8d8d8}
.spine-text{position:absolute;left:50%;top:0;transform-origin:left top;transform:rotate(90deg) translateY(-50%);white-space:nowrap;color:var(--white);font-family:"Roboto",sans-serif;font-weight:700}
.spine-title{top:82px;font-size:22px;letter-spacing:.5px}
.spine-author{top:466px;font-size:17px;letter-spacing:3px}

/* front cover */
.front{position:absolute;left:582px;top:0;width:548px;height:825px;overflow:hidden}
.front-photo{position:absolute;inset:0;background:
  radial-gradient(ellipse 40% 55% at 40% 60%,var(--photo-light),var(--photo-mid) 55%,transparent 80%),
  radial-gradient(ellipse 30% 40% at 70% 40%,rgba(185,185,185,.8),transparent 70%),
  linear-gradient(180deg,var(--photo-dark),#3b3b3b 60%,#555)}
.author{position:absolute;top:36px;left:0;width:100%;text-align:center;color:var(--white);font-family:"Roboto",sans-serif;font-weight:700;font-size:18px;letter-spacing:2px}
.title{position:absolute;top:82px;left:0;width:100%;text-align:center;color:var(--title-red);font-family:"Roboto",sans-serif;font-weight:900;font-size:68px;line-height:72px;text-transform:uppercase;letter-spacing:-.5px}
.subtitle-band{position:absolute;left:0;top:589px;width:548px;height:72px;background:linear-gradient(90deg,var(--band-blue-dark),var(--band-blue) 40%,var(--band-blue-light));display:flex;align-items:center;justify-content:center;text-align:center;color:var(--white);font-family:"Open Sans",sans-serif;font-style:italic;font-weight:700;font-size:15px;line-height:22px}
</style>
</head>
<body>
<div class="wrap">
  <div class="cover">
    <section class="back">
      <div class="back-photo" role="img" aria-label="Faint dark photograph of a person covering their eyes with their hands"></div>
      <div class="praise praise-1">
        <blockquote>Dorian Wexcombe offers expert insight and a transparent evaluation in this book. With years of healthy involvement with that which is right in the body of Christ, he can speak to both the personal and systematic issues that cause bad environments to develop. The church landscape is littered with people who have been hurt in churches. This book will help clean things up.</blockquote>
        <cite>–Marlon Tessaly, Senior Pastor, Cedar Hollow Fellowship, Alder Falls, VT. cedarhollowfc.org</cite>
      </div>
      <div class="praise praise-2">
        <blockquote>“Seldom, if ever, have<br>I read a book that was so refreshingly personal and real, yet delivered material that put you in a position to navigate the difficult and damaging challenges, of being part of a degenerating church. I was moved to tears and then lifted to a place of hope, by the pain and abuse that this family faced and their incredible testimony and journey of recovery. All glory to the power of His love for us.”</blockquote>
        <cite>– Ruth Adeyemi-Loft, Kestrel Path Ministries, kestrelpathjourney.org</cite>
      </div>
      <div class="praise praise-3">
        <blockquote>“Dorian Wexcombe offers a real-world view on how following your spiritual calling is not always easy but completely worth the journey. His down to earth approach allows the reader to process and be encouraged by his personal story, insight, and commitment to faith.”</blockquote>
        <cite>– Lena Morrowfield, Executive Director, Harbor Nine Ministry, Inc. harbornine.org</cite>
      </div>
      <div class="praise praise-4">
        <blockquote>“Dorian Wexcombe has been a pastor over 40 years. I have known him personally for many of those years. This book is a case study of how trust can be abused. Dorian handles this difficult issue with a good balance of honest introspection and critical analysis of leadership structures and practices. This book is a must-read.”</blockquote>
        <cite>– –Gideon R. Paxley, ReasonedHope.net</cite>
      </div>
      <div class="author-photo" role="img" aria-label="Portrait photograph of the author"></div>
      <p class="bio">Dorian Wexcombe is a long-time pastor, author and podcaster who has impacted leaders and churches for many years. He wrote Iceberg Ahead, a study of church leadership drawn from the history of the legendary ship. He and his wife Miriam, together with their grown children and spouses all serve in ministry.</p>
    </section>

    <section class="spine">
      <span class="spine-text spine-title">QUIET LANTERNS</span>
      <span class="spine-text spine-author">Dorian T. Wexcombe</span>
    </section>

    <section class="front">
      <div class="front-photo" role="img" aria-label="Black and white photograph of a person with a hand covering their eyes"></div>
      <p class="author">Dorian T. Wexcombe</p>
      <h1 class="title">Quiet<br>Lanterns</h1>
      <p class="subtitle-band">Ways To Notice and Step Away From<br>Harmful Circles While Keeping Steady Belief</p>
    </section>
  </div>
</div>
</body>
</html>
```